Brava-Lux.ch is looking for business card letterhead and envelope C5 with WOW effect

We need a strong business card for our company Brava-Lux.ch, logo is available. You want a black or dark background on which the logo Stark r% 26 # 252; appears. Letterhead and envelope in C5 format should be in a similar design, but does not have to be We need a strong business card for our company Brava-Lux.ch, logo is available. A black or dark background is desired, on which the logo Stark comes across. The letterhead and the envelope in C5 format should have a similar design.

Target Market(s)

Private customers as well as entrepreneurs

Contact Information for Business Card

E-mail: info@brava-lux.ch
Web.www.Brava-Lux.ch
Tel: +41 ( 0 ) 79 384 6027
Adresse:
Kellerweg 14
9405 Ostheim

Hier kann man Icons verwenden für Email,Tel und Adressse

Font styles to use
Other font styles liked:
• Dubai,bold

Colors

Designer to choose colors to be used in the design.

Requirements
Must have
• WOW effect
Nice to have
• R% 26 # 252; back business card with our service listings. - VEHICLE LABELING - SHOP WINDOW LABELING - STICKERS AND MUCH MORE ... in red color

```html
<!DOCTYPE html>
<html lang="de">
<head>
<meta charset="utf-8">
<title>Brava-Lux.ch – Visitenkarte</title>
<link rel="stylesheet" href="https://fonts.googleapis.com/css2?family=Open+Sans:wght@400;600;800&display=swap">
<style>
  :root {
    --backdrop: #e7e5e1;
    --card: #ffffff;
    --ink: #1b1b1b;
    --honey: #f2c113;
    --honey-soft: #f6d24a;
  }
  * { box-sizing: border-box; margin: 0; padding: 0; }
  html, body {
    width: 1200px;
    height: 843px;
    overflow: hidden;
    background: var(--backdrop);
    font-family: "Open Sans", Arial, sans-serif;
    color: var(--ink);
  }
  .sheet {
    width: 1200px;
    height: 843px;
    display: flex;
    align-items: center;
    justify-content: center;
    gap: 40px;
  }
  .card {
    position: relative;
    width: 540px;
    height: 315px;
    background: var(--card);
    box-shadow: 0 6px 18px rgba(0,0,0,.12);
    overflow: hidden;
  }

  /* front */
  .edge-bar {
    position: absolute;
    left: 0;
    width: 10px;
  }
  .edge-bar--honey { top: 40px; height: 80px; background: var(--honey); }
  .edge-bar--ink { top: 278px; height: 30px; background: var(--ink); }

  .contact-list {
    position: absolute;
    left: 44px;
    top: 26px;
    list-style: none;
    font-size: 15px;
    font-weight: 600;
    line-height: 24px;
  }
  .contact-list li { display: flex; align-items: center; gap: 12px; }
  .contact-list svg { width: 16px; height: 16px; flex: none; }

  .brand {
    position: absolute;
    display: flex;
    align-items: center;
    gap: 14px;
  }
  .brand--front { left: 150px; top: 140px; }
  .brand-dot {
    width: 46px;
    height: 46px;
    border-radius: 50%;
    background: var(--honey);
  }
  .brand-name {
    font-weight: 800;
    font-size: 34px;
    letter-spacing: 1px;
    text-transform: uppercase;
    color: var(--ink);
  }

  .address {
    position: absolute;
    left: 44px;
    bottom: 26px;
    display: flex;
    align-items: center;
    gap: 14px;
    font-size: 15px;
    font-weight: 600;
    line-height: 20px;
  }
  .address svg { width: 18px; height: 20px; }

  /* back */
  .honeycomb {
    position: absolute;
    left: 0;
    top: 0;
    width: 540px;
    height: 315px;
  }
  .brand--back {
    right: 38px;
    top: 34px;
    flex-direction: column;
    align-items: center;
    gap: 2px;
  }
  .brand-web {
    font-size: 14px;
    font-weight: 600;
    letter-spacing: 5px;
  }
</style>
</head>
<body>
<main class="sheet">

  <section class="card card--front" aria-label="Vorderseite">
    <span class="edge-bar edge-bar--honey"></span>
    <span class="edge-bar edge-bar--ink"></span>

    <ul class="contact-list">
      <li>
        <svg viewBox="0 0 24 24" fill="none" stroke="#f2c113" stroke-width="2"><path d="M5 3h4l2 5-3 2a12 12 0 0 0 6 6l2-3 5 2v4a2 2 0 0 1-2 2A17 17 0 0 1 3 5a2 2 0 0 1 2-2z"/></svg>
        +41 ( 0 ) 79 384 6027
      </li>
      <li>
        <svg viewBox="0 0 24 24" fill="none" stroke="#f2c113" stroke-width="2"><rect x="3" y="5" width="18" height="14"/><path d="M3 5l9 8 9-8"/></svg>
        info@brava-lux.ch
      </li>
      <li>
        <svg viewBox="0 0 24 24" fill="none" stroke="#f2c113" stroke-width="2"><circle cx="12" cy="12" r="9"/><path d="M3 12h18M12 3c3 3 3 15 0 18M12 3c-3 3-3 15 0 18"/></svg>
        www.Brava-Lux.ch
      </li>
    </ul>

    <div class="brand brand--front">
      <span class="brand-dot"></span>
      <span class="brand-name">Brava-Lux.ch</span>
    </div>

    <div class="address">
      <svg viewBox="0 0 24 26" fill="none" stroke="#f2c113" stroke-width="2"><path d="M12 24s-8-8-8-14a8 8 0 0 1 16 0c0 6-8 14-8 14z"/><circle cx="12" cy="10" r="3"/></svg>
      <span>Kellerweg 14<br>9405 Ostheim</span>
    </div>
  </section>

  <section class="card card--back" aria-label="Rückseite">
    <svg class="honeycomb" viewBox="0 0 540 315" role="img" aria-label="Dekoratives Wabenmuster in Gelb">
      <defs>
        <linearGradient id="honey-fade" x1="0" y1="1" x2="1" y2="0">
          <stop offset="0" stop-color="#f2c113"/>
          <stop offset="1" stop-color="#f6d24a"/>
        </linearGradient>
      </defs>
      <polygon points="0,20 150,20 200,110 370,150 390,230 300,265 180,315 0,315" fill="url(#honey-fade)"/>
    </svg>

    <div class="brand brand--back">
      <span class="brand-name">Brava-Lux.ch</span>
      <span class="brand-web">www.Brava-Lux.ch</span>
    </div>
  </section>

</main>
</body>
</html>
```